Alaska Law Firm Needs a Sticker Design

We need a design for stickers to put on already-printed brochures. We mail the brochures to potential clients so they can learn more about accident-induced injuries, insurance claims, legal representation, and our own law firm.

One of our lawyers wrote a book that provides a helpful overview of personal injury claims. We are offering this book for free to anyone who calls and requests it. Therefore, the sticker design should include one of the following phrases, or something very similar:
a) "Still have questions? Call and request our book-- for free!"
b) "Still have questions about auto accident claims? Call and request our book today."
c) "Still have questions about filing a claim? Call and request a free copy of our book."
d) "Still have questions? Call us today to request a free copy of our book, Clear Lanes Ahead."
e) "To learn more about automobile accidents and insurance, call today and request a free copy of our book."

The sticker should be approximately 3"x3" and may be a circle, square, rectangle, or ellipsis. The sticker will be placed on the back of the folder, which is light blue. We would like the sticker to match the color scheme of our website and the folder.

I will upload an image of the book cover as soon as I obtain it.

Industry/Entity Type

Law Firm

Font styles to use
Serif
Sans Serif

Requirements
Should not have
• Bright colors that aren't already used in the folder design. e.g. no bright orange, pink, chartreuse, turquoise, yellow, red.

```html
<!DOCTYPE html>
<html lang="en">
<head>
<meta charset="utf-8">
<title>Still Have Questions Sticker</title>
<link rel="stylesheet" href="https://fonts.googleapis.com/css2?family=Play:wght@400;700&family=Gabriela&display=swap">
<style>
  :root {
    --page-bg: #ececec;
    --navy: #1f2e86;
    --navy-deep: #18236d;
    --band: #1e2d80;
    --ink: #1c1c1c;
    --frame-line: #262626;
    --paper: #ffffff;
    --script-blue: #213394;
  }
  html, body {
    margin: 0;
    padding: 0;
    width: 1200px;
    height: 1200px;
    overflow: hidden;
    background: var(--page-bg);
  }
  .sticker {
    display: block;
    width: 1200px;
    height: 1200px;
  }
  .sticker-edge { fill: var(--navy); }
  .sticker-face { fill: var(--paper); }
  .panel { fill: var(--paper); stroke: var(--frame-line); stroke-width: 3.5; }
  .headline-band { fill: var(--band); }
  .lead-in {
    font-family: "Play", sans-serif;
    font-weight: 700;
    font-size: 92px;
    fill: var(--ink);
  }
  .question-word {
    font-family: "Play", sans-serif;
    font-weight: 700;
    font-size: 108px;
    fill: var(--paper);
  }
  .offer-line {
    font-family: "Gabriela", serif;
    font-size: 41px;
    fill: var(--ink);
  }
  .offer-highlight {
    font-family: "Gabriela", serif;
    font-size: 150px;
    fill: var(--script-blue);
  }
</style>
</head>
<body>
<svg class="sticker" viewBox="0 0 1200 1200" xmlns="http://www.w3.org/2000/svg" role="img" aria-label="Sticker: Still have Questions? Call and request our book for free!">
  <rect class="sticker-edge" x="180" y="231" width="840" height="720" rx="120" ry="120"/>
  <rect class="sticker-face" x="197" y="248" width="806" height="686" rx="104" ry="104"/>

  <path class="panel" d="M218 428 V352 Q218 268 302 268 H898 Q982 268 982 352 V428 Z"/>
  <rect class="headline-band" x="196" y="441" width="808" height="140"/>
  <path class="panel" d="M218 593 H982 V830 Q982 914 898 914 H302 Q218 914 218 830 Z"/>

  <text class="lead-in" x="608" y="380" text-anchor="middle">Still have</text>
  <text class="question-word" x="606" y="546" text-anchor="middle">Questions?</text>
  <text class="offer-line" x="604" y="666" text-anchor="middle">Call and request our book</text>
  <text class="offer-highlight" x="604" y="830" text-anchor="middle">for free!</text>
</svg>
</body>
</html>
```